Eye Doctor Needs Updated Business Card

We need a standard US business card designed for an optometrist's practice. Our practice name is Halvick Sight Center and attached you'll find our logos. We are located in a smaller community, we are a trusted source for eye care and designer eyewear. We have 2 different version of our logos, so both versions are attached. Our slogan is "Small Town Values, World Class Care". I'd like to see designs with one of our logos on the front with our contact info, and have the slogan on the back by itself. Final design should be professional looking, include the colors of our logo or colors that compliment the logo. We want it to look appropriate for a healthcare practice but also up-to-date, eye-catching, to have the normal contact info like address, phone #, email, but also possibly room for additional contact info such as facebook.
Updates

I just uploaded .eps files to use instead of the jpeg. Hope that helps!

So many great designs! We tending to like the darker blues that are used in our logo as the main blue color for the business cards. We also really like the use of a water-mark type appearance on either the front and/or back, or the embossed look as well looks nice. Thank you all for such great designs!

We're preferring the designs where white and the darker blue used in our logo are the primary colors on the front, but with a little green used as well. Again though, thanks for all the impressive designs so far!

Industry/Entity Type

Healthcare

```html
<!DOCTYPE html>
<html lang="en">
<head>
<meta charset="utf-8">
<title>Halvick Sight Center – Business Card</title>
<link rel="stylesheet" href="https://fonts.googleapis.com/css2?family=Mulish:ital,wght@0,400;0,600;0,700;1,400&display=swap">
<style>
  :root {
    --page: #d9d9d9;
    --card-white: #ffffff;
    --brand-blue: #1d5f8f;
    --back-blue-top: #2a7fb0;
    --back-blue-bottom: #1a5e8c;
    --brand-green: #4a7a12;
    --leaf-green: #5fa32a;
    --ink: #4a4a4a;
    --ink-soft: #6a6a6a;
    --divider: #c9c9c9;
  }
  * { margin: 0; padding: 0; box-sizing: border-box; }
  html, body { width: 1200px; height: 871px; overflow: hidden; }
  body {
    background: var(--page);
    font-family: "Mulish", sans-serif;
    position: relative;
  }
  .card {
    position: absolute;
    width: 640px;
    height: 366px;
    border-radius: 2px;
    box-shadow: 0 6px 18px rgba(0,0,0,0.25);
    overflow: hidden;
  }
  /* Front */
  .card--front { left: 280px; top: 40px; background: var(--card-white); }
  .brand-block {
    position: absolute; left: 40px; top: 70px; width: 260px;
    display: flex; flex-direction: column; align-items: center;
  }
  .brand-dot {
    width: 88px; height: 88px; border-radius: 50%;
    background: var(--brand-blue);
    margin-bottom: 18px;
  }
  .brand-name {
    color: var(--brand-blue);
    font-weight: 700;
    font-size: 24px;
    letter-spacing: 1px;
    text-transform: uppercase;
    text-align: center;
    line-height: 1.2;
  }
  .divider {
    position: absolute; left: 318px; top: 36px; width: 1px; height: 228px;
    background: linear-gradient(to bottom, transparent, var(--divider) 30%, var(--divider) 70%, transparent);
  }
  .contact { position: absolute; left: 352px; top: 50px; color: var(--ink); }
  .contact__name { font-weight: 700; font-size: 20px; color: var(--ink); }
  .contact__title { font-size: 14px; color: var(--brand-green); margin-top: 4px; }
  .contact__address { font-size: 13px; color: var(--ink-soft); margin-top: 26px; line-height: 1.35; }
  .contact__list { list-style: none; margin-top: 8px; font-size: 13px; color: var(--ink-soft); }
  .contact__list li { display: flex; align-items: center; gap: 10px; height: 22px; }
  .contact__list svg { width: 13px; height: 13px; flex: none; }
  .band-stripe { position: absolute; left: 0; bottom: 64px; width: 100%; height: 6px; background: var(--brand-blue); }
  .band {
    position: absolute; left: 0; bottom: 0; width: 100%; height: 64px;
    background: var(--brand-green);
    display: flex; align-items: center; padding-left: 140px; gap: 14px;
    color: #ffffff; font-size: 16px; letter-spacing: 0.5px;
  }
  .band__square { width: 14px; height: 14px; background: #ffffff; border-radius: 2px; }
  /* Back */
  .card--back {
    left: 280px; top: 460px;
    background: linear-gradient(to bottom, var(--back-blue-top), var(--back-blue-bottom));
    display: flex; align-items: center; justify-content: center; gap: 18px;
  }
  .slogan-dot { width: 28px; height: 28px; border-radius: 50%; background: var(--leaf-green); flex: none; }
  .slogan {
    color: #ffffff;
    font-weight: 600;
    font-size: 26px;
    letter-spacing: 0.5px;
    line-height: 1.3;
  }
</style>
</head>
<body>
  <section class="card card--front">
    <div class="brand-block">
      <div class="brand-dot"></div>
      <div class="brand-name">Halvick Sight Center</div>
    </div>
    <div class="divider"></div>
    <div class="contact">
      <div class="contact__name">Marlo Penhurst</div>
      <div class="contact__title">Owner/Optometrist</div>
      <div class="contact__address">4410 W. Alder Rd. Ste. 202<br>Bramwell, Az. 85999</div>
      <ul class="contact__list">
        <li><svg viewBox="0 0 16 16"><path fill="#4a7a12" d="M3 1h3l1.5 4-2 1.2a9 9 0 0 0 4.3 4.3L11 8.5l4 1.5v3a2 2 0 0 1-2 2A12 12 0 0 1 1 3a2 2 0 0 1 2-2z"/></svg>555.204.1187</li>
        <li><svg viewBox="0 0 16 16"><rect x="1" y="3" width="14" height="10" rx="1" fill="#4a7a12"/><path d="M1.5 3.5 8 9l6.5-5.5" stroke="#fff" stroke-width="1.3" fill="none"/></svg>hello@halvicksight.com</li>
        <li><svg viewBox="0 0 16 16"><circle cx="8" cy="8" r="7" fill="#4a7a12"/><path d="M1 8h14M8 1c3 3.5 3 10.5 0 14M8 1c-3 3.5-3 10.5 0 14" stroke="#fff" stroke-width="1" fill="none"/></svg>www.halvicksightcenter.com</li>
      </ul>
    </div>
    <div class="band-stripe"></div>
    <div class="band"><span class="band__square"></span>www.halvicksightcenter.com</div>
  </section>

  <section class="card card--back">
    <div class="slogan-dot"></div>
    <p class="slogan">Small Town Values, World Class Care</p>
  </section>
</body>
</html>
```